Business Card for a finance professional

I need a business card design to introduce myself to a professional networking (mainly banks) and potential companies to hire and remember me. I would like to use black, grey, white and maybe gold/silver colors and maybe something with my initials(R L F P T). The final design should communicate seriousness, profissionalism and something innovative.

The basic informations in the card are: Name, e-mail, phone number and trabnet. (I'm thinking to put some directly short link to my trabnet account or maybe some app - non QR Code - to add my contacts to a phone directly.)

My name is Mariana Lopes Ferreira Pinto dos Reis (I prefer to use only 'Mariana Lopes' or 'Mariana Reis' but i'm open to other suggestions) and I have 26 years old (just if it helps to build based in my age).
Updates

Dear designers, I wish to thank your participation in this project! It was very difficult to choose one! Thank your for your work! Best regards and success. Mariana

Target Market(s)

Potential hires and big companies.

Industry/Entity Type

Finance

Requirements
Must have
• The informations required at the business card are:
Name: Mariana Lopes F. P. dos Reis
Email: mariana.lop.reis@quellomail.com
Phone: +55 61 8493 5710
TrabNet: http://br.trabnet-perfis.com/in/marianalr/
Nice to have
• Modern and innovative look.
I suggest to use the colors black, grey, white, gold and/or silver, but I'm open to other colors.
Should not have
• A message showing that I need to be hired. It's more to "know me and remember me" than "hire me please".

```html
<!DOCTYPE html>
<html lang="en">
<head>
<meta charset="utf-8">
<title>Mariana Lopes — Business Card</title>
<link rel="stylesheet" href="https://fonts.googleapis.com/css2?family=Montserrat:wght@300;400;500&family=Lato:wght@400;700&display=swap">
<style>
  :root {
    --page: #e9e9e9;
    --card-white: #f7f7f5;
    --card-grey: #a9a7a9;
    --panel-dark: #333436;
    --panel-grey: #9c9a9c;
    --accent-green: #8fd46f;
    --ink: #2f2f31;
    --ink-soft: #b9b9b9;
    --rule-dark: #3a3b3d;
  }
  * { box-sizing: border-box; margin: 0; padding: 0; }
  html, body {
    width: 1200px; height: 900px; overflow: hidden;
    background: var(--page);
  }
  .sheet {
    width: 1200px; height: 900px;
    display: flex; flex-direction: column; align-items: center; justify-content: center;
    gap: 40px;
  }
  .card {
    position: relative;
    width: 640px; height: 366px;
    overflow: hidden;
    box-shadow: 0 6px 18px rgba(0,0,0,.18);
  }
  .card-front { background: var(--card-white); }
  .card-back { background: var(--card-grey); }
  .card-shapes { position: absolute; inset: 0; width: 100%; height: 100%; }

  .name {
    font-family: "Montserrat", sans-serif;
    font-weight: 300;
    letter-spacing: .02em;
    color: var(--ink);
    text-transform: uppercase;
    white-space: nowrap;
  }
  .name-accent { color: var(--accent-green); font-weight: 500; }

  .front-identity { position: absolute; left: 92px; top: 62px; }
  .front-identity .name { font-size: 27px; line-height: 1; }
  .full-name {
    font-family: "Montserrat", sans-serif;
    font-weight: 400;
    font-size: 10.5px;
    letter-spacing: .04em;
    text-transform: uppercase;
    color: var(--ink-soft);
    margin-top: 4px;
  }

  .contact-list {
    position: absolute; left: 44px; top: 212px;
    list-style: none;
    font-family: "Lato", sans-serif;
    font-size: 14.5px;
    color: var(--ink);
  }
  .contact-item { display: flex; align-items: center; height: 23px; }
  .contact-icon { width: 20px; height: 16px; margin-right: 14px; flex: none; }

  .back-identity {
    position: absolute; right: 44px; top: 246px;
  }
  .back-identity .name { font-size: 24px; }
</style>
</head>
<body>
<main class="sheet">

  <section class="card card-front" aria-label="Card front">
    <svg class="card-shapes" viewBox="0 0 640 366" aria-hidden="true">
      <polygon points="442,168 640,168 640,366 598,366" fill="var(--panel-grey)"/>
      <line x1="460" y1="196" x2="598" y2="366" stroke="var(--accent-green)" stroke-width="3"/>
      <polygon points="392,0 640,0 640,222 556,236" fill="var(--panel-dark)"/>
      <line x1="0" y1="298" x2="470" y2="319" stroke="var(--accent-green)" stroke-width="3"/>
      <line x1="470" y1="319" x2="580" y2="324" stroke="var(--rule-dark)" stroke-width="3"/>
    </svg>

    <div class="front-identity">
      <h1 class="name">Mariana <span class="name-accent">Lopes</span></h1>
      <p class="full-name">Ferreira Pinto dos Reis</p>
    </div>

    <ul class="contact-list">
      <li class="contact-item">
        <svg class="contact-icon" viewBox="0 0 20 16" aria-hidden="true">
          <rect x="6" y="2" width="8" height="13" rx="1.2" fill="var(--ink)"/>
          <rect x="7.5" y="4" width="5" height="4" fill="var(--card-white)"/>
          <rect x="11" y="0" width="1.5" height="3" fill="var(--ink)"/>
        </svg>
        <span>+55 61 8493 5710</span>
      </li>
      <li class="contact-item">
        <svg class="contact-icon" viewBox="0 0 20 16" aria-hidden="true">
          <rect x="1.5" y="2.5" width="17" height="11" fill="none" stroke="var(--ink)" stroke-width="1.4"/>
          <polyline points="1.5,2.5 10,9.5 18.5,2.5" fill="none" stroke="var(--ink)" stroke-width="1.4"/>
        </svg>
        <span>mariana.lop.reis@quellomail.com</span>
      </li>
      <li class="contact-item">
        <svg class="contact-icon" viewBox="0 0 20 16" aria-hidden="true">
          <rect x="2" y="0" width="16" height="16" rx="2" fill="var(--ink)"/>
        </svg>
        <span>http://br.trabnet-perfis.com/in/marianalr</span>
      </li>
    </ul>
  </section>

  <section class="card card-back" aria-label="Card back">
    <svg class="card-shapes" viewBox="0 0 640 366" aria-hidden="true">
      <polygon points="0,0 200,0 148,366 0,366" fill="var(--panel-dark)"/>
      <polygon points="158,210 176,210 176,366 150,366" fill="#dcdcdc"/>
      <line x1="192" y1="150" x2="170" y2="366" stroke="var(--accent-green)" stroke-width="3"/>
      <line x1="300" y1="296" x2="350" y2="296" stroke="#f3f3f3" stroke-width="3"/>
      <line x1="350" y1="296" x2="640" y2="296" stroke="var(--accent-green)" stroke-width="3"/>
    </svg>

    <div class="back-identity">
      <p class="name">Mariana <span class="name-accent">Lopes</span></p>
    </div>
  </section>

</main>
</body>
</html>
```